looking for sleek business card to standout from the crowd!

We are a young biotechnology company looking to help you personalize your health through understanding your genetic make up. We need you help in making a clean but sleek business card design using our new logo. The goal? Any time we give our cards out, people say "nice card!" The feel we are going for is "modern-techy". We don't want to come across as an old, giant pharma company, but not trying to be a hipster either.

Target Market(s)

healthcare and biotechnology industry.

Industry/Entity Type

Biotechnology

Contact Information for Business Card

Info to include on the card will be NAME, TITLE, EMAIL, PHONE. The companies website (www.corvalinbio.com) should also be on the card some where. Would like the logo, when printed, to be raised.

Requirements
Must have
• The logo we have attached in the color it is in. Fonts for text should lean toward more professional/tech.
Nice to have
• Prefer white/light color background
Should not have
• cartoons, landscape backgrounds images.

```html
<!DOCTYPE html>
<html lang="en">
<head>
<meta charset="utf-8">
<title>Corvalin – Business Card</title>
<link rel="stylesheet" href="https://fonts.googleapis.com/css2?family=Open+Sans:wght@400;600&display=swap">
<style>
  :root {
    --brand-blue: #1b75bc;
    --brand-green: #8cc63f;
    --ink: #4a4a4a;
    --paper: #ffffff;
    --stage: #e9e7e3;
    --rule: #cfcfcf;
  }
  * { margin: 0; padding: 0; box-sizing: border-box; }
  html, body {
    width: 1200px;
    height: 987px;
    overflow: hidden;
    background: var(--stage);
    font-family: "Open Sans", Arial, sans-serif;
  }
  .card {
    position: absolute;
    left: 292px;
    width: 616px;
    height: 351px;
    box-shadow: 0 2px 6px rgba(0,0,0,0.18);
  }
  .card--front { top: 130px; background: var(--paper); }
  .card--back { top: 505px; width: 614px; background: var(--brand-green); }

  .brand-name {
    position: absolute;
    font-weight: 600;
    font-size: 36px;
    letter-spacing: 1px;
    line-height: 1;
  }
  .card--front .brand-name { left: 50px; top: 160px; color: var(--brand-blue); }
  .card--back .brand-name { right: 38px; top: 256px; color: #fff; }

  .divider {
    position: absolute;
    left: 303px;
    top: 110px;
    width: 1px;
    height: 130px;
    background: var(--rule);
  }
  .contact { position: absolute; left: 327px; top: 109px; }
  .contact__name {
    font-size: 21px;
    font-weight: 600;
    color: var(--brand-blue);
    line-height: 1.2;
  }
  .contact__title {
    font-size: 16px;
    color: var(--brand-green);
    line-height: 1.3;
    margin-bottom: 10px;
  }
  .contact__list { list-style: none; }
  .contact__item {
    display: flex;
    align-items: center;
    gap: 9px;
    font-size: 16px;
    color: var(--ink);
    line-height: 23.5px;
  }
  .contact__icon { width: 14px; height: 14px; fill: var(--brand-blue); flex: none; }

  .stripe { position: absolute; left: 0; width: 100%; }
  .stripe--green { top: 333px; height: 2px; background: var(--brand-green); }
  .stripe--blue { top: 336px; height: 15px; background: var(--brand-blue); }

  .card__web {
    position: absolute;
    right: 38px;
    top: 310px;
    font-size: 16px;
    color: #fff;
  }
</style>
</head>
<body>
  <section class="card card--front" aria-label="Business card front">
    <p class="brand-name">CORVALIN</p>
    <div class="divider"></div>
    <div class="contact">
      <p class="contact__name">MARA ELLISON</p>
      <p class="contact__title">CEO/Founder</p>
      <ul class="contact__list">
        <li class="contact__item">
          <svg class="contact__icon" viewBox="0 0 24 24" aria-hidden="true"><path d="M6.6 10.8a15.1 15.1 0 0 0 6.6 6.6l2.2-2.2c.3-.3.7-.4 1-.2 1.1.4 2.3.6 3.6.6.6 0 1 .4 1 1V20c0 .6-.4 1-1 1A17 17 0 0 1 3 4c0-.6.4-1 1-1h3.5c.6 0 1 .4 1 1 0 1.3.2 2.5.6 3.6.1.3 0 .7-.2 1z"/></svg>
          <span>415 555 0192</span>
        </li>
        <li class="contact__item">
          <svg class="contact__icon" viewBox="0 0 24 24" aria-hidden="true"><path d="M2 5h20v2l-10 6.5L2 7z"/><path d="M2 9l10 6.5L22 9v10H2z"/></svg>
          <span>mellison@corvalinbio.com</span>
        </li>
        <li class="contact__item">
          <svg class="contact__icon" viewBox="0 0 24 24" aria-hidden="true"><circle cx="12" cy="12" r="10"/><path d="M2 12h20M12 2c3 3 3 17 0 20M12 2c-3 3-3 17 0 20" fill="none" stroke="#fff" stroke-width="1.4"/></svg>
          <span>www.corvalinbio.com</span>
        </li>
      </ul>
    </div>
    <div class="stripe stripe--green"></div>
    <div class="stripe stripe--blue"></div>
  </section>

  <section class="card card--back" aria-label="Business card back">
    <p class="brand-name">CORVALIN</p>
    <p class="card__web">www.corvalinbio.com</p>
  </section>
</body>
</html>
```